Stationary (Business Cards, envelopes, cover letters, etc) for HARBOR LANTERN PARTNERS
The Harbor Lantern Partners
Stationary (Business Cards, envelopes, cover letters, etc) for HARBOR LANTERN PARTNERS - Business Opportunities
Creative Brief
Professional
Rodrigo Velasco Brennan
Av. Ignacio Marroquín 718 B Col. Los Pinos Altos México DF CP 01482 México
rvelasco@hlp-example.mx
www.hlp-example.mx
First impressions have high impact, so in terms of the business card, it has to be something that's out of the box. The card is used to present ourselves to another party or prospect, but it also has to have a high impact message, either by an image or a phrase that comes attached in the back side. It could be some key points of a preview success case. So the back side has to have a marketing application. It has to be a card that will stand out, so much that it will be shown and passed around. In design and in materials (maybe???), although win the materials it will have a high impact on the costs of production. It has to be standard size, so it fits in every wallet thus avoiding on being thrown somewhere.
Concepts
Business Card and Stationary Project for a multifaceted corporation
Stationary for holding company
Business cards for RFTV - Investimentos e Administrações
mitiha mitiha
GREAT NEWS! WE'VE EXTENDED TO THIS FRIDAY! KEEP UP THE GREAT WORK!!!
Hi designers! GREAT JOB! We are want to decide today (our time) the winner. Please if you have any questions, let us know. Try to show as much applications as possible, i.e. we're now in a digital world so some digital applications we'll be considered for higher points. Have seen proposals in blue and gray (predominant colors and mixed), but none in orange. Let's see some! *Don't use curved lines in your design proposals. THANKS!
Hi, first of all I want to thank each and every one of you for accepting in working on our project. GREAT DESIGNS !!!!! Something we don't want is the lines that make a "curve" to separate content. I've seen a lot of those in the market and we want to be ORIGINAL. As I said in the brief, we want our cards to be saved as something awsome, and to be shown to other people. Material: sent your proposals of other materials, however if you can also send the specificatiosn of that material so we can see the cost of printing in them. Remember that it's not only the business cards but the stationary. KEEP UP THE GREAT JOB! CREATE DESIGN!

```html
<!DOCTYPE html>
<html lang="en">
<head>
<meta charset="utf-8">
<title>The Harbor Lantern Partners — Stationery</title>
<link href="https://fonts.googleapis.com/css2?family=Cinzel:wght@400;600&family=Open+Sans:wght@400;600&display=swap" rel="stylesheet">
<style>
  :root {
    --backdrop: #8e8e8e;
    --paper: #ffffff;
    --ink: #141414;
    --brand-blue: #1f9fd8;
    --brand-orange: #f08a24;
    --rule: #c9c9c9;
    --faint: #dfe9f1;
    --text-grey: #555;
  }
  * { box-sizing: border-box; margin: 0; padding: 0; }
  html, body { width: 1200px; height: 490px; overflow: hidden; }
  body {
    background: var(--backdrop);
    position: relative;
    font-family: "Open Sans", Arial, sans-serif;
    color: var(--ink);
  }
  .piece { position: absolute; background: var(--paper); box-shadow: 0 2px 4px rgba(0,0,0,.25); overflow: hidden; }
  .wordmark { font-family: "Cinzel", Georgia, serif; font-weight: 600; letter-spacing: .04em; line-height: 1.15; }
  .mark-square { display: inline-block; background: var(--brand-blue); }
  .side-band { position: absolute; left: 0; top: 0; bottom: 0; background: var(--ink); }
  .side-band::before { content: ""; position: absolute; left: 0; right: 0; top: 8%; height: 9%; background: var(--brand-blue); }
  .faint-square { position: absolute; background: var(--faint); }
  .small { font-size: 4px; color: var(--text-grey); line-height: 1.4; }

  /* folder */
  .folder { position: absolute; left: 20px; top: 40px; width: 450px; height: 420px; }
  .folder svg { position: absolute; inset: 0; }
  .folder-cover { position: absolute; left: 20px; top: 10px; width: 212px; height: 262px; padding: 22px 16px; color: #fff; text-align: center; }
  .folder-cover .wordmark { font-size: 12px; color: #fff; }
  .folder-cover .mark-square { width: 90px; height: 90px; margin-top: 40px; }
  .folder-inside { position: absolute; left: 232px; top: 10px; width: 212px; height: 262px; }
  .folder-inside .head { position: absolute; left: 18px; top: 14px; font-size: 6px; }
  .folder-pocket-label { position: absolute; top: 385px; font-size: 5px; width: 110px; text-align: center; }

  /* disc */
  .disc { position: absolute; left: 478px; top: 28px; width: 92px; height: 92px; border-radius: 50%; background: var(--paper); box-shadow: 0 2px 4px rgba(0,0,0,.25); }
  .disc::after { content: ""; position: absolute; left: 38px; top: 38px; width: 16px; height: 16px; border-radius: 50%; background: var(--backdrop); }
  .disc .mark-square { position: absolute; left: 10px; top: 30px; width: 14px; height: 14px; }

  .sleeve { left: 574px; top: 22px; width: 190px; height: 130px; }
  .card { height: 42px; }
  .card-front { left: 636px; top: 110px; width: 72px; }
  .card-back { left: 714px; top: 110px; width: 72px; }
  .slip { left: 800px; top: 22px; width: 120px; height: 130px; }

  .sheet { top: 170px; width: 128px; height: 250px; }
  .sheet .head { position: absolute; left: 14px; top: 8px; font-size: 5px; }
  .letter-lines { position: absolute; left: 20px; right: 12px; top: 60px; }
  .letter-lines span { display: block; height: 1px; background: var(--rule); margin-bottom: 6px; }
  .form-table { position: absolute; left: 16px; top: 40px; width: 100px; border-collapse: collapse; font-size: 4px; }
  .form-table td { border: .5px solid #999; height: 7px; padding: 0 2px; }

  .envelope { left: 932px; width: 254px; }
  .env-front { top: 172px; height: 112px; }
  .env-back { top: 298px; height: 118px; }
  .env-back svg { position: absolute; inset: 0; }
</style>
</head>
<body>

  <!-- presentation folder -->
  <div class="folder">
    <svg width="450" height="420" viewBox="0 0 450 420">
      <polygon points="0,150 20,140 20,272 0,262" fill="#fff"/>
      <rect x="20" y="10" width="212" height="262" fill="var(--ink)"/>
      <rect x="232" y="10" width="212" height="262" fill="#fff"/>
      <polygon points="20,272 232,272 232,415 40,415 20,330" fill="#fff"/>
      <polygon points="232,272 444,272 444,330 424,415 232,415" fill="#fff"/>
      <line x1="232" y1="272" x2="232" y2="415" stroke="var(--rule)"/>
      <line x1="20" y1="272" x2="444" y2="272" stroke="var(--rule)"/>
    </svg>
    <div class="folder-cover">
      <div class="wordmark">THE HARBOR LANTERN PARTNERS</div>
      <span class="mark-square"></span>
    </div>
    <div class="folder-inside">
      <div class="faint-square" style="left:110px;top:150px;width:80px;height:80px"></div>
    </div>
    <div class="folder-pocket-label wordmark" style="left:60px">HARBOR LANTERN PARTNERS</div>
    <div class="folder-pocket-label wordmark" style="left:290px">HARBOR LANTERN PARTNERS</div>
  </div>

  <!-- disc -->
  <div class="disc"><span class="mark-square"></span></div>

  <!-- disc sleeve -->
  <div class="piece sleeve">
    <div class="side-band" style="width:14px"></div>
    <div class="wordmark" style="position:absolute;left:22px;top:10px;font-size:5px">HARBOR LANTERN PARTNERS</div>
    <div class="faint-square" style="right:12px;bottom:12px;width:46px;height:46px"></div>
  </div>

  <!-- business cards -->
  <div class="piece card card-front">
    <div class="side-band" style="width:6px"></div>
    <div class="wordmark" style="position:absolute;left:10px;top:6px;font-size:4px"><span class="mark-square" style="width:8px;height:8px;vertical-align:middle"></span> HARBOR LANTERN</div>
    <div class="small" style="position:absolute;left:10px;bottom:4px;font-size:3px">Rodrigo Velasco Brennan<br>rvelasco@hlp-example.mx</div>
  </div>
  <div class="piece card card-back">
    <div class="side-band" style="width:6px"></div>
    <div class="small" style="position:absolute;left:10px;top:6px;font-size:3px">Rodrigo Velasco Brennan<br>Av. Ignacio Marroquín 718 B<br>www.hlp-example.mx</div>
  </div>

  <!-- compliment slip -->
  <div class="piece slip">
    <div class="side-band" style="width:10px"></div>
    <div class="wordmark" style="position:absolute;left:16px;top:8px;font-size:4px">HARBOR LANTERN PARTNERS</div>
    <div class="small" style="position:absolute;left:16px;bottom:6px;font-size:3px">www.hlp-example.mx</div>
  </div>

  <!-- letterheads -->
  <div class="piece sheet" style="left:500px">
    <div class="side-band" style="width:8px"></div>
    <div class="wordmark head">HARBOR LANTERN PARTNERS</div>
    <table class="form-table">
      <tr><td>Date</td><td></td><td>Client</td><td></td></tr>
      <tr><td>Project</td><td></td><td>Ref</td><td></td></tr>
      <tr><td></td><td></td><td></td><td></td></tr>
      <tr><td></td><td></td><td></td><td></td></tr>
    </table>
    <div class="faint-square" style="right:10px;bottom:14px;width:50px;height:50px"></div>
  </div>
  <div class="piece sheet" style="left:640px">
    <div class="side-band" style="width:8px"></div>
    <div class="wordmark head">HARBOR LANTERN PARTNERS</div>
    <div class="letter-lines"><span></span><span></span><span></span><span></span><span></span><span></span><span></span></div>
    <div class="faint-square" style="right:10px;bottom:14px;width:50px;height:50px"></div>
  </div>
  <div class="piece sheet" style="left:780px">
    <div class="side-band" style="width:8px"></div>
    <div class="wordmark head">HARBOR LANTERN PARTNERS</div>
    <div class="faint-square" style="right:10px;bottom:14px;width:50px;height:50px"></div>
    <div class="small" style="position:absolute;left:14px;bottom:6px;font-size:3px">Av. Ignacio Marroquín 718 B Col. Los Pinos Altos México DF CP 01482 México</div>
  </div>

  <!-- envelopes -->
  <div class="piece envelope env-front">
    <div class="side-band" style="width:12px"></div>
    <div class="wordmark" style="position:absolute;left:20px;top:10px;font-size:5px">HARBOR LANTERN PARTNERS</div>
    <div class="small" style="position:absolute;left:20px;top:20px;font-size:3px">Av. Ignacio Marroquín 718 B Col. Los Pinos Altos México DF CP 01482 México</div>
  </div>
  <div class="piece envelope env-back">
    <svg width="254" height="118" viewBox="0 0 254 118">
      <polygon points="0,0 254,0 254,14 127,74 0,14" fill="var(--ink)"/>
      <polyline points="0,118 127,60 254,118" fill="none" stroke="var(--rule)"/>
    </svg>
    <div class="wordmark" style="position:absolute;left:0;right:0;top:82px;text-align:center;font-size:5px">HARBOR LANTERN PARTNERS</div>
  </div>

</body>
</html>
```